Vitamin B12 Liquid Drops Label

hi, i need a label designed for my vitamin b12 drops that i am going to be selling on bazaroo. the label needs to quickly capture the attention of a buyer as he or she is scrolling through the thumbnail search results on bazaroo.example my brand is called zulpa. i already have an example brand logo i will be using, however, i need help designing the rest of the label. attached are some examples of labels i like for other supplements.some of these examples are pink. i do not want pink. please go for a blue/green color scheme. THE DESIGN MUST BE BOLD

Target Market(s)

adults ages 30 - 64

Font styles to use
Sans Serif

Colors
0455a3
cedeed
3176b5
85acd3
cfdeed
9bcb3b
abd037
cadf82
00a990

Requirements
Must have
• - bold design
• - somewhat gender-neutral color scheme because this will be used equally by men and women
• - B12 MUST be very prominent and visible on the label
Should not have
• - it should not be "crunchy" looking

```html
<!DOCTYPE html>
<html lang="en">
<head>
<meta charset="utf-8">
<title>Zulpa B-12 Drops Label</title>
<link rel="stylesheet" href="https://fonts.googleapis.com/css2?family=Archivo+Black&family=Fira+Sans:wght@800&family=Fira+Sans+Condensed:wght@600&family=Open+Sans:wght@700&display=swap">
<style>
  :root {
    --navy: #1c2a5c;
    --navy-deep: #1a2756;
    --royal: #24428f;
    --badge: #223a80;
    --sky: #2bb4ea;
    --sky-soft: #8fd8f5;
    --paper: #f6f6f6;
    --paper-shade: #e9eaec;
    --white: #ffffff;
  }
  html, body {
    margin: 0;
    padding: 0;
    width: 790px;
    height: 1200px;
    overflow: hidden;
    background: var(--paper);
  }
  .label {
    position: relative;
    width: 790px;
    height: 1200px;
    overflow: hidden;
    background: radial-gradient(ellipse at 70% 30%, var(--white) 0%, var(--paper) 55%, var(--paper-shade) 100%);
    font-family: "Open Sans", Arial, sans-serif;
  }
  .brand-strip {
    position: absolute;
    left: 0;
    top: 0;
    width: 272px;
    height: 1200px;
    background: linear-gradient(180deg, var(--navy) 0%, var(--navy-deep) 100%);
  }
  .brand-strip::after {
    content: "";
    position: absolute;
    right: -8px;
    top: 0;
    width: 8px;
    height: 100%;
    background: repeating-linear-gradient(180deg, var(--navy) 0 3px, var(--white) 3px 6px);
  }
  .brand-name {
    position: absolute;
    left: 140px;
    top: 470px;
    transform: translate(-50%, -50%) rotate(-90deg);
    font-family: "Archivo Black", "Arial Black", sans-serif;
    font-size: 214px;
    line-height: 1;
    letter-spacing: 0;
    color: var(--white);
    white-space: nowrap;
  }
  .product {
    position: absolute;
    left: 326px;
    top: 432px;
    width: 450px;
  }
  .product-name {
    margin: 0;
    font-family: "Fira Sans", Arial, sans-serif;
    font-weight: 800;
    font-size: 192px;
    line-height: 1;
    letter-spacing: -2px;
    color: var(--navy);
    white-space: nowrap;
  }
  .product-type {
    margin: 0 0 0 6px;
    font-size: 31px;
    font-weight: 700;
    letter-spacing: 1px;
    color: var(--navy);
    white-space: nowrap;
  }
  .waves {
    position: absolute;
    left: 0;
    top: 0;
    width: 790px;
    height: 1200px;
  }
  .volume {
    position: absolute;
    left: 620px;
    top: 978px;
    width: 142px;
    height: 156px;
    border-radius: 16px;
    background: var(--badge);
    color: var(--white);
    text-align: center;
    font-family: "Fira Sans Condensed", Arial, sans-serif;
    font-weight: 600;
    font-size: 40px;
    line-height: 1.5;
    padding-top: 18px;
    box-sizing: border-box;
  }
</style>
</head>
<body>
  <main class="label">
    <div class="brand-strip">
      <div class="brand-name">ZULPA</div>
    </div>

    <section class="product">
      <h1 class="product-name">B-12</h1>
      <p class="product-type">DIETRY SUPPLEMENT</p>
    </section>

    <svg class="waves" viewBox="0 0 790 1200" aria-hidden="true">
      <defs>
        <linearGradient id="skyBand" x1="0" y1="0" x2="1" y2="0">
          <stop offset="0" stop-color="#2bb4ea"/>
          <stop offset="1" stop-color="#8fd8f5"/>
        </linearGradient>
        <linearGradient id="navyBand" x1="0" y1="0" x2="0" y2="1">
          <stop offset="0" stop-color="#24428f"/>
          <stop offset="1" stop-color="#1a2756"/>
        </linearGradient>
      </defs>
      <path d="M0 935 C 250 975, 450 905, 600 805 C 680 752, 740 722, 790 710 L 790 1200 L 0 1200 Z" fill="url(#skyBand)"/>
      <path d="M0 1000 C 250 1012, 450 962, 600 885 C 680 845, 740 830, 790 825 L 790 1200 L 0 1200 Z" fill="url(#navyBand)"/>
    </svg>

    <div class="volume">2<br>FL OZ</div>
  </main>
</body>
</html>
```